Quillmore Website design

Create a sophisticated minimalist shopify ecommerce store that can be integrated with stockwise hub POS.

Quillmore is a Brick and mortar store that is focused on exceptional customer service and quality Ladies fashion and specialty swimwear for Women, Men and Children.

This website will need to be easy to navigate by the end user and manage inhouse.

With so many different product categories and customer demographics it will be difficult to make seamless and easy to navigate.

Think The Varnel, Lumo etc where there are Women, Men and Kids

It would be fantastic to build a site with three different navigations to constant themes that are modified to suit each demographic.

We have a logo to use and would like the theme to be easily updated as seasons change and our business evolves.

The website must be set up to use SEO for google and other leading search engines.

Stock will be supplied from either our brick and mortar store or warehouse so would need to consist of multiple store locations as far as the back end is concerned.

It will need to be set up with apps that allow us to stream line our fullfilment in house (label printing, picking lists and shipping with Kestrel Freight)

```html
<!DOCTYPE html>
<html lang="en">
<head>
<meta charset="utf-8">
<title>Quillmore – Coastal Fashion</title>
<link rel="stylesheet" href="https://fonts.googleapis.com/css2?family=Montserrat:wght@400;500;600;700&display=swap">
<style>
:root{
  --olive-dark:#5f6954;
  --olive:#7b8569;
  --sage:#8f9e7f;
  --ink:#1d1d1d;
  --muted:#6d6d6d;
  --line:#dcdcdc;
  --panel:#f4f4f4;
  --white:#ffffff;
  --star:#f39a1e;
}
*{box-sizing:border-box;margin:0;padding:0}
html,body{width:1200px;height:4080px;overflow:hidden}
body{position:relative;font-family:'Montserrat',sans-serif;color:var(--ink);background:var(--white)}
.abs{position:absolute}

.announce{left:0;top:0;width:1200px;height:47px;background:var(--olive-dark);overflow:hidden;white-space:nowrap;color:#fff;font-size:14px;line-height:47px}
.announce .track{position:absolute;left:-72px;top:0;display:flex;gap:34px}

.header{left:0;top:47px;width:1200px;height:99px;border-bottom:1px solid var(--line)}
.logo{left:50%;top:28px;transform:translateX(-50%);display:flex;align-items:center;gap:8px;font-size:22px;font-weight:500;letter-spacing:3px;color:var(--sage)}
.logo .dot{width:12px;height:12px;border-radius:50%;background:var(--sage)}
.hicon{top:30px}
.cart-count{left:1068px;top:37px;font-size:14px;color:var(--muted)}
.nav{left:0;top:146px;width:1200px;height:44px;display:flex;justify-content:center;align-items:center;gap:20px;font-size:15px;color:#444}
.nav .sep{color:#999}

.hero{left:0;top:190px;width:1200px;height:504px;background:linear-gradient(90deg,#5f5f5f 0%,#8a8a8a 45%,#b9b9b7 70%,#d4d3d0 100%)}
.hero h1{left:111px;top:90px;font-size:45px;line-height:52px;font-weight:600;color:#fff;white-space:nowrap;letter-spacing:-0.3px}
.hero p{left:111px;top:272px;width:470px;font-size:16.5px;line-height:26px;color:#fff}
.btn{display:flex;align-items:center;justify-content:center;gap:6px;background:var(--sage);color:#fff;font-size:15px;font-weight:500;border-radius:5px}
.hero .btn{left:111px;top:364px;width:169px;height:36px}
.btn .i{width:15px;height:15px;border-radius:50%;background:#fff;display:inline-block;position:relative}
.btn .i::after{content:"";position:absolute;left:4px;top:4px;width:5px;height:5px;border-top:1.5px solid var(--sage);border-right:1.5px solid var(--sage)}

.section-title{left:0;width:1200px;text-align:center;font-size:37px;font-weight:500}

.cat{width:301px}
.cat .photo{height:323px;border-radius:14px}
.cat .label{margin-top:12px;height:54px;border:1.5px solid #bbb;border-radius:12px;display:flex;align-items:center;justify-content:space-between;padding:0 10px;font-size:20px;font-weight:500}
.go{width:28px;height:28px;border-radius:50%;background:var(--olive);display:flex;align-items:center;justify-content:center}

.tabs{left:111px;top:1412px;width:978px;height:50px;border-bottom:1px solid var(--line);font-size:19px;font-weight:500}
.tabs span{position:absolute;top:4px}
.tabs .active{border-bottom:3px solid var(--ink);padding-bottom:14px}

.prod{width:301px}
.prod .card{position:relative;height:323px;border-radius:12px;background:var(--panel)}
.prod .card.sel{border:2px solid #7a7a7a}
.prod .shot{position:absolute;left:70px;right:70px;top:30px;height:215px;border-radius:10px}
.prod .tools{position:absolute;left:0;right:0;top:266px;display:flex;justify-content:center;gap:12px}
.tool{width:32px;height:32px;border-radius:50%;background:#fff;display:flex;align-items:center;justify-content:center;box-shadow:0 1px 3px rgba(0,0,0,.12)}
.tool.on{background:var(--sage)}
.prod h3{margin-top:14px;text-align:center;font-size:21px;font-weight:500}
.prod .price{margin-top:6px;text-align:center;font-size:14px;color:#333}
.sw{margin-top:14px;display:flex;justify-content:center;gap:12px}
.sw i{width:24px;height:24px;border-radius:50%;display:block}

.promo{left:0;top:2492px;width:1200px;height:451px;background:linear-gradient(180deg,#b8cfdb 0%,#d7e2e6 55%,#e8e6df 100%)}
.promo .figure{left:140px;top:20px;width:430px;height:431px;background:radial-gradient(ellipse at 50% 55%,#f07a3c 0%,#e8a17a 45%,rgba(232,200,180,0) 75%)}
.promo .eyebrow{right:111px;top:110px;text-align:right;font-size:27px;line-height:38px;font-weight:500;white-space:nowrap}
.promo .big{right:111px;top:210px;font-size:64px;font-weight:700}
.promo .btn{left:920px;top:291px;width:169px;height:37px}

.tcard{top:3106px;width:285px;height:305px;background:#fff;border-radius:10px;box-shadow:0 2px 12px rgba(0,0,0,.1);padding:26px 24px}
.stars{display:flex;gap:2px}
.gmark{position:absolute;right:16px;top:16px;width:30px;height:30px;border-radius:50%;border:4px solid #4a86e8}
.tcard p{margin-top:18px;font-size:12.5px;line-height:20px;color:#555}
.who{position:absolute;left:24px;top:220px;display:flex;align-items:center;gap:14px}
.avatar{width:60px;height:60px;border-radius:50%;background:var(--olive);color:#fff;font-size:26px;font-weight:600;display:flex;align-items:center;justify-content:center}
.who b{display:block;font-size:15px;font-weight:600}
.who small{font-size:11px;color:#777}
.dots{left:0;top:3452px;width:1200px;display:flex;justify-content:center;gap:8px;align-items:center}
.dots i{width:10px;height:10px;border-radius:50%;background:#888;display:block}
.dots i.on{width:14px;height:14px;background:var(--olive)}

.footer{left:0;top:3696px;width:1200px;height:384px;background:var(--olive);color:#fff}
.promise{left:73px;top:3622px;width:1053px;height:125px;background:#fff;border:1px solid var(--line);display:flex;align-items:center;justify-content:space-around;padding:0 20px}
.pitem{display:flex;align-items:center;gap:14px}
.pitem b{display:block;font-size:17px;font-weight:500}
.pitem small{font-size:14px;color:#666}
.flogo{left:111px;top:3840px;font-size:24px;font-weight:500;letter-spacing:3px;color:#cfd6c4}
.fabout{left:111px;top:3922px;width:240px;font-size:15.5px;line-height:22px;word-spacing:5px}
.fcol{top:3806px}
.fcol h4{font-size:19px;font-weight:500;margin-bottom:16px}
.fcol li{list-style:none;font-size:14.5px;line-height:27.5px;color:#eef0ea}
.fcol li::before{content:"»";margin-right:12px;font-size:18px}
.news p{font-size:15px;line-height:25px;margin-top:-2px;width:250px}
.email{margin-top:20px;width:251px;height:32px;background:#fff;border-radius:3px;display:flex;align-items:center;justify-content:space-between;padding:0 10px 0 14px;font-size:12px;color:#999}
.copy{left:111px;top:4034px;font-size:12.5px}
.pay{left:885px;top:4030px;display:flex;gap:4px}
.pay i{width:30px;height:18px;background:#fff;border-radius:2px;display:block}
</style>
</head>
<body>

<div class="abs announce">
  <div class="track">
    <span>Shop Now for Limited-Time Discounts!</span><span>|</span>
    <span>Enjoy a Free Gift with Every Purchase!</span><span>|</span>
    <span>Shop Now for Limited-Time Discounts!</span><span>|</span>
    <span>Enjoy a Free Gift with Every Purchase!</span>
  </div>
</div>

<header class="abs header">
  <svg class="abs hicon" style="left:111px" width="28" height="28" viewBox="0 0 24 24" fill="none" stroke="#333" stroke-width="2.4"><circle cx="10" cy="10" r="7"/><path d="M15 15l6 6"/></svg>
  <div class="abs logo"><span class="dot"></span>QUILLMORE</div>
  <svg class="abs hicon" style="left:925px" width="28" height="28" viewBox="0 0 24 24" fill="none" stroke="#555" stroke-width="1.5"><circle cx="12" cy="8" r="4.5"/><path d="M3.5 21c1-4.5 4.5-7 8.5-7s7.5 2.5 8.5 7"/></svg>
  <svg class="abs hicon" style="left:977px" width="36" height="32" viewBox="0 0 28 24" fill="none" stroke="#555" stroke-width="1.6"><path d="M12 20s-9-5.5-9-11.5A4.8 4.8 0 0 1 12 6a4.8 4.8 0 0 1 9 2.5C21 14.5 12 20 12 20z"/><circle cx="21" cy="17" r="5" fill="var(--olive)" stroke="none"/><text x="21" y="19.5" font-size="7" fill="#fff" text-anchor="middle" font-family="Montserrat,sans-serif" stroke="none">0</text></svg>
  <svg class="abs hicon" style="left:1034px" width="28" height="28" viewBox="0 0 24 24" fill="none" stroke="#555" stroke-width="1.6"><rect x="3.5" y="7" width="17" height="14" rx="2"/><path d="M8 10V6a4 4 0 0 1 8 0v4"/></svg>
  <span class="abs cart-count">(0)</span>
</header>

<nav class="abs nav">
  <span>Women</span><span class="sep">|</span><span>Men</span><span class="sep">|</span><span>Kids</span><span class="sep">|</span><span>New Arrivals</span><span class="sep">|</span><span>Sale</span><span class="sep">|</span><span>About</span><span class="sep">|</span><span>Stores</span>
</nav>

<section class="abs hero" role="img" aria-label="Woman in sunglasses and a checked coat against a concrete wall">
  <h1 class="abs">Luxe Women’s<br>Fashion Tailored For<br>Coastal Getaways</h1>
  <p class="abs">From chic swimwear to elegant resort pieces, explore fashion-forward styles for women who love quality, comfort, and sophisticated beach living.</p>
  <a class="abs btn">Shop Women <span class="i"></span></a>
</section>

<h2 class="abs section-title" style="top:772px">Our Categories</h2>
<div class="abs cat" style="left:111px;top:860px">
  <div class="photo" role="img" aria-label="Woman in white swimwear relaxing on the sand" style="background:linear-gradient(160deg,#d9c3a5,#c9a987 60%,#e4d6c4)"></div>
  <div class="label">Women <span class="go"><svg width="12" height="12" viewBox="0 0 12 12" fill="none" stroke="#fff" stroke-width="1.8"><path d="M3 9l6-6M4 3h5v5"/></svg></span></div>
</div>
<div class="abs cat" style="left:450px;top:860px">
  <div class="photo" role="img" aria-label="Man in navy swim shorts standing in clear blue sea" style="background:linear-gradient(180deg,#8fd0ea 0%,#35aee0 45%,#1597d0 100%)"></div>
  <div class="label">Men <span class="go"><svg width="12" height="12" viewBox="0 0 12 12" fill="none" stroke="#fff" stroke-width="1.8"><path d="M3 9l6-6M4 3h5v5"/></svg></span></div>
</div>
<div class="abs cat" style="left:788px;top:860px">
  <div class="photo" role="img" aria-label="Two girls in swimsuits jumping off a jetty into a lake" style="background:linear-gradient(180deg,#8ec6e4 0%,#b5d4de 45%,#5f8a6a 75%,#3d6f82 100%)"></div>
  <div class="label">Kids <span class="go"><svg width="12" height="12" viewBox="0 0 12 12" fill="none" stroke="#fff" stroke-width="1.8"><path d="M3 9l6-6M4 3h5v5"/></svg></span></div>
</div>

<h2 class="abs section-title" style="top:1328px">Trending Collections</h2>
<div class="abs tabs">
  <span class="active" style="left:142px">Swimwear</span>
  <span style="left:328px">Dresses &amp; Resort Wear</span>
  <span style="left:634px">New Season Arrivals</span>
</div>

<div class="abs prod" style="left:111px;top:1513px">
  <div class="card sel"><div class="shot" role="img" aria-label="Red triangle bikini" style="background:radial-gradient(ellipse,#c85a5a 0%,#d88a8a 45%,rgba(244,244,244,0) 72%)"></div>
    <div class="tools"><span class="tool on"><svg width="16" height="16" viewBox="0 0 24 24" fill="none" stroke="#fff" stroke-width="2"><rect x="4" y="8" width="16" height="13" rx="2"/><path d="M8 10V7a4 4 0 0 1 8 0v3"/></svg></span><span class="tool"><svg width="16" height="16" viewBox="0 0 24 24" fill="none" stroke="#333" stroke-width="2"><path d="M2 12s4-7 10-7 10 7 10 7-4 7-10 7S2 12 2 12z"/><circle cx="12" cy="12" r="3"/></svg></span><span class="tool"><svg width="16" height="16" viewBox="0 0 24 24" fill="none" stroke="#333" stroke-width="2"><path d="M12 20s-9-5.5-9-11.5A4.8 4.8 0 0 1 12 6a4.8 4.8 0 0 1 9 2.5C21 14.5 12 20 12 20z"/></svg></span></div></div>
  <h3>Linen Resort Midi</h3><div class="price">$21.00</div>
  <div class="sw"><i style="background:#d05f5f"></i><i style="background:#f2550e"></i><i style="background:#c0500f"></i></div>
</div>
<div class="abs prod" style="left:450px;top:1513px">
  <div class="card"><div class="shot" role="img" aria-label="Rainbow striped swim shorts" style="background:linear-gradient(180deg,rgba(244,244,244,0) 8%,#4fc04a 18%,#1e8fe0 35%,#f7c230 60%,#f2441c 80%,rgba(244,244,244,0) 92%)"></div>
    <div class="tools"><span class="tool"><svg width="16" height="16" viewBox="0 0 24 24" fill="none" stroke="#333" stroke-width="2"><rect x="4" y="8" width="16" height="13" rx="2"/><path d="M8 10V7a4 4 0 0 1 8 0v3"/></svg></span><span class="tool"><svg width="16" height="16" viewBox="0 0 24 24" fill="none" stroke="#333" stroke-width="2"><path d="M2 12s4-7 10-7 10 7 10 7-4 7-10 7S2 12 2 12z"/><circle cx="12" cy="12" r="3"/></svg></span><span class="tool"><svg width="16" height="16" viewBox="0 0 24 24" fill="none" stroke="#333" stroke-width="2"><path d="M12 20s-9-5.5-9-11.5A4.8 4.8 0 0 1 12 6a4.8 4.8 0 0 1 9 2.5C21 14.5 12 20 12 20z"/></svg></span></div></div>
  <h3>Linen Resort Midi</h3><div class="price">$21.00</div>
  <div class="sw"><i style="background:#d05f5f"></i><i style="background:#f2550e"></i><i style="background:#c0500f"></i></div>
</div>
<div class="abs prod" style="left:788px;top:1513px">
  <div class="card"><div class="shot" role="img" aria-label="Coral palm print swim shorts" style="background:radial-gradient(ellipse,#f0605a 0%,#f07a74 45%,rgba(244,244,244,0) 72%)"></div>
    <div class="tools"><span class="tool"><svg width="16" height="16" viewBox="0 0 24 24" fill="none" stroke="#333" stroke-width="2"><rect x="4" y="8" width="16" height="13" rx="2"/><path d="M8 10V7a4 4 0 0 1 8 0v3"/></svg></span><span class="tool"><svg width="16" height="16" viewBox="0 0 24 24" fill="none" stroke="#333" stroke-width="2"><path d="M2 12s4-7 10-7 10 7 10 7-4 7-10 7S2 12 2 12z"/><circle cx="12" cy="12" r="3"/></svg></span><span class="tool"><svg width="16" height="16" viewBox="0 0 24 24" fill="none" stroke="#333" stroke-width="2"><path d="M12 20s-9-5.5-9-11.5A4.8 4.8 0 0 1 12 6a4.8 4.8 0 0 1 9 2.5C21 14.5 12 20 12 20z"/></svg></span></div></div>
  <h3>Linen Resort Midi</h3><div class="price">$21.00</div>
  <div class="sw"><i style="background:#f26161"></i><i style="background:#f2550e"></i><i style="background:#c0500f"></i></div>
</div>

<div class="abs prod" style="left:111px;top:1980px">
  <div class="card"><div class="shot" role="img" aria-label="Floral print one-piece swimsuit" style="background:radial-gradient(ellipse,#7d4aa0 0%,#d860a0 35%,#e6b04a 55%,rgba(244,244,244,0) 72%)"></div>
    <div class="tools"><span class="tool"><svg width="16" height="16" viewBox="0 0 24 24" fill="none" stroke="#333" stroke-width="2"><rect x="4" y="8" width="16" height="13" rx="2"/><path d="M8 10V7a4 4 0 0 1 8 0v3"/></svg></span><span class="tool"><svg width="16" height="16" viewBox="0 0 24 24" fill="none" stroke="#333" stroke-width="2"><path d="M2 12s4-7 10-7 10 7 10 7-4 7-10 7S2 12 2 12z"/><circle cx="12" cy="12" r="3"/></svg></span><span class="tool"><svg width="16" height="16" viewBox="0 0 24 24" fill="none" stroke="#333" stroke-width="2"><path d="M12 20s-9-5.5-9-11.5A4.8 4.8 0 0 1 12 6a4.8 4.8 0 0 1 9 2.5C21 14.5 12 20 12 20z"/></svg></span></div></div>
  <h3>Linen Resort Midi</h3><div class="price">$21.00</div>
  <div class="sw"><i style="background:#d05f5f"></i><i style="background:#e3a4d8"></i><i style="background:#c0500f"></i></div>
</div>
<div class="abs prod" style="left:450px;top:1980px">
  <div class="card"><div class="shot" role="img" aria-label="Black one-piece swimsuit with orange trim" style="background:radial-gradient(ellipse,#3a2226 0%,#4a2a26 40%,#f08a40 55%,rgba(244,244,244,0) 72%)"></div>
    <div class="tools"><span class="tool"><svg width="16" height="16" viewBox="0 0 24 24" fill="none" stroke="#333" stroke-width="2"><rect x="4" y="8" width="16" height="13" rx="2"/><path d="M8 10V7a4 4 0 0 1 8 0v3"/></svg></span><span class="tool"><svg width="16" height="16" viewBox="0 0 24 24" fill="none" stroke="#333" stroke-width="2"><path d="M2 12s4-7 10-7 10 7 10 7-4 7-10 7S2 12 2 12z"/><circle cx="12" cy="12" r="3"/></svg></span><span class="tool"><svg width="16" height="16" viewBox="0 0 24 24" fill="none" stroke="#333" stroke-width="2"><path d="M12 20s-9-5.5-9-11.5A4.8 4.8 0 0 1 12 6a4.8 4.8 0 0 1 9 2.5C21 14.5 12 20 12 20z"/></svg></span></div></div>
  <h3>Linen Resort Midi</h3><div class="price">$21.00</div>
  <div class="sw"><i style="background:#d05f5f"></i><i style="background:#3a2226"></i><i style="background:#c0500f"></i></div>
</div>
<div class="abs prod" style="left:788px;top:1980px">
  <div class="card"><div class="shot" role="img" aria-label="Bright red swim shorts" style="background:radial-gradient(ellipse,#f2461f 0%,#f4643f 45%,rgba(244,244,244,0) 72%)"></div>
    <div class="tools"><span class="tool"><svg width="16" height="16" viewBox="0 0 24 24" fill="none" stroke="#333" stroke-width="2"><rect x="4" y="8" width="16" height="13" rx="2"/><path d="M8 10V7a4 4 0 0 1 8 0v3"/></svg></span><span class="tool"><svg width="16" height="16" viewBox="0 0 24 24" fill="none" stroke="#333" stroke-width="2"><path d="M2 12s4-7 10-7 10 7 10 7-4 7-10 7S2 12 2 12z"/><circle cx="12" cy="12" r="3"/></svg></span><span class="tool"><svg width="16" height="16" viewBox="0 0 24 24" fill="none" stroke="#333" stroke-width="2"><path d="M12 20s-9-5.5-9-11.5A4.8 4.8 0 0 1 12 6a4.8 4.8 0 0 1 9 2.5C21 14.5 12 20 12 20z"/></svg></span></div></div>
  <h3>Linen Resort Midi</h3><div class="price">$21.00</div>
  <div class="sw"><i style="background:#d05f5f"></i><i style="background:#f2550e"></i><i style="background:#f0301a"></i></div>
</div>

<section class="abs promo">
  <div class="abs figure" role="img" aria-label="Woman in an orange bikini and sheer orange shirt under a bright sky"></div>
  <div class="abs eyebrow">Beach Holiday Essentials – Curated<br>by Quillmore</div>
  <div class="abs big">30% Off</div>
  <a class="abs btn">Shop Women <span class="i"></span></a>
</section>

<h2 class="abs section-title" style="top:3022px">Testimonials</h2>
<div class="abs tcard" style="left:111px">
  <div class="stars"><svg width="86" height="16" viewBox="0 0 86 16" fill="var(--star)"><path id="st" d="M8 1l2.1 4.5 4.9.6-3.6 3.4.9 4.9L8 12l-4.3 2.4.9-4.9L1 6.1l4.9-.6z"/><use href="#st" x="17"/><use href="#st" x="34"/><use href="#st" x="51"/><use href="#st" x="68"/></svg></div>
  <span class="gmark"></span>
  <p>Lorem ipsum dolor sit amet, cons ectetur adipiscing elit, sed do eiusm od tempor incididunt ut labore et dolore magna aliqua. Ut enim ad minim veniam, quis nostrud exercitation ullamco laboris nisi ut aliquip ex</p>
  <div class="who"><span class="avatar">RB</span><div><b>Randall Benston</b><small>CEO, ABC Group</small></div></div>
</div>
<div class="abs tcard" style="left:457px">
  <div class="stars"><svg width="86" height="16" viewBox="0 0 86 16" fill="var(--star)"><use href="#st"/><use href="#st" x="17"/><use href="#st" x="34"/><use href="#st" x="51"/><use href="#st" x="68"/></svg></div>
  <span class="gmark"></span>
  <p>Lorem ipsum dolor sit amet, cons ectetur adipiscing elit, sed do eiusm od tempor incididunt ut labore et dolore magna aliqua. Ut enim ad minim veniam, quis nostrud exercitation ullamco laboris nisi ut aliquip ex</p>
  <div class="who"><span class="avatar">RB</span><div><b>Randall Benston</b><small>CEO, ABC Group</small></div></div>
</div>
<div class="abs tcard" style="left:803px">
  <div class="stars"><svg width="86" height="16" viewBox="0 0 86 16" fill="var(--star)"><use href="#st"/><use href="#st" x="17"/><use href="#st" x="34"/><use href="#st" x="51"/><use href="#st" x="68"/></svg></div>
  <span class="gmark"></span>
  <p>Lorem ipsum dolor sit amet, cons ectetur adipiscing elit, sed do eiusm od tempor incididunt ut labore et dolore magna aliqua. Ut enim ad minim veniam, quis nostrud exercitation ullamco laboris nisi ut aliquip ex</p>
  <div class="who"><span class="avatar">RB</span><div><b>Randall Benston</b><small>CEO, ABC Group</small></div></div>
</div>
<div class="abs dots"><i class="on"></i><i></i><i></i><i></i></div>

<h2 class="abs section-title" style="top:3546px">Brand Promise</h2>

<footer class="abs footer"></footer>

<div class="abs promise">
  <div class="pitem"><svg width="54" height="40" viewBox="0 0 54 40" fill="none" stroke="#333" stroke-width="1.8"><rect x="8" y="6" width="26" height="22" rx="2"/><path d="M34 13h9l7 8v7H34"/><circle cx="16" cy="31" r="4"/><circle cx="42" cy="31" r="4"/><path d="M2 14h10M4 20h8M15 16l4 4 7-8"/></svg><div><b>Free Shipping</b><small>On all orders over $49.00</small></div></div>
  <div class="pitem"><svg width="40" height="44" viewBox="0 0 40 44" fill="none" stroke="#333" stroke-width="1.8"><path d="M14 4h12l-4 8h-4z"/><path d="M16 12C6 18 4 28 6 34c2 6 26 6 28 0 2-6 0-16-10-22"/><text x="20" y="32" font-size="14" text-anchor="middle" fill="#333" stroke="none" font-family="Montserrat,sans-serif">$</text></svg><div><b>15 Days Returns</b><small>Moneyback guarantee</small></div></div>
  <div class="pitem"><svg width="44" height="40" viewBox="0 0 44 40" fill="none" stroke="#333" stroke-width="1.8"><rect x="4" y="12" width="30" height="20" rx="2" transform="rotate(-25 19 22)"/><path d="M6 22l28-13"/><rect x="14" y="20" width="26" height="16" rx="2"/><path d="M18 28h10"/></svg><div><b>Secure Checkout</b><small>Protected by Tillpoint Pay</small></div></div>
  <div class="pitem"><svg width="48" height="40" viewBox="0 0 48 40" fill="none" stroke="#333" stroke-width="1.8"><rect x="6" y="10" width="30" height="20" rx="2"/><rect x="14" y="16" width="30" height="20" rx="2"/><circle cx="29" cy="26" r="4"/><path d="M6 17h30"/></svg><div><b>Offer &amp; Gift Here</b><small>On all orders over</small></div></div>
</div>

<div class="abs flogo">QUILLMORE</div>
<p class="abs fabout" style="color:#fff">Lorem ipsum dolor sit amet, cons ect etur adipiscing</p>

<div class="abs fcol" style="left:408px">
  <h4>Useful Links</h4>
  <ul><li>My Account</li><li>Shopping cart</li><li>Wishlist</li><li>Custom Link</li><li>Help</li></ul>
</div>
<div class="abs fcol" style="left:601px">
  <h4>Information</h4>
  <ul><li>Shipping &amp; Returns</li><li>Secure Shopping</li><li>Affiliates</li><li>FAQs</li><li>Contact</li></ul>
</div>
<div class="abs fcol news" style="left:836px">
  <h4>Newsletter</h4>
  <p>Subscribe to our newsletter to receive news on update.</p>
  <div class="email">Enter your email <svg width="18" height="12" viewBox="0 0 18 12" fill="none" stroke="#222" stroke-width="1.8"><path d="M1 6h15M11 1l5 5-5 5"/></svg></div>
</div>

<div class="abs copy" style="color:#fff">Copyright © 2025 Quillmore. All Right Reserved.</div>
<div class="abs pay"><i></i><i></i><i></i><i></i><i></i><i></i></div>

</body>
</html>
```